2 Creative Website Banners for Furniture Brand

Morning Tobrasca....
The get a great night sleep banner is complete - we are happy with that one.
Ive uploaded a slightly different concept for the other banner below. This is just something rough ive thrown together. But you can see I have added a curve, a maroon coloured background which is slightly transparent and a big heart in the background....
I do not necessarily want to use this heart image but something a bit like this (a nice graphic, gif etc) but something quite elegant faded in, or perhaps a number of hearts (done in a tasteful way). Also can we keep the typography in the same format as you can see for this one.
Nearly there :)!
Industry/Entity Type
Furniture

```html
<!DOCTYPE html>
<html lang="en">
<head>
<meta charset="utf-8">
<title>Find a Look You Love – Bedrooms Banner</title>
<link rel="stylesheet" href="https://fonts.googleapis.com/css2?family=Poppins:wght@300;400&family=Playfair+Display:wght@400&family=Crimson+Text:wght@400&display=swap">
<style>
  :root {
    --mauve: #6e6367;
    --mauve-light: #7a6f73;
    --mauve-dark: #625858;
    --ink-white: #ffffff;
    --button-text: #5b5257;
    --heart: #ffffff;
  }
  * { margin: 0; padding: 0; box-sizing: border-box; }
  html, body {
    width: 1200px;
    height: 356px;
    overflow: hidden;
    background: var(--mauve);
  }
  .banner {
    position: relative;
    width: 1200px;
    height: 356px;
    overflow: hidden;
    background: linear-gradient(90deg, var(--mauve-dark) 0%, var(--mauve) 40%, var(--mauve-light) 60%);
  }
  .banner__hearts {
    position: absolute;
    inset: 0;
    width: 1200px;
    height: 356px;
  }
  .banner__hearts path {
    fill: none;
    stroke: var(--heart);
    stroke-width: 1.5;
  }
  .banner__photo {
    position: absolute;
    inset: 0;
    width: 1200px;
    height: 356px;
  }
  .banner__copy {
    position: absolute;
    left: 170px;
    top: 45px;
    width: 320px;
    text-align: center;
    color: var(--ink-white);
  }
  .banner__kicker {
    font-family: "Poppins", sans-serif;
    font-weight: 300;
    font-size: 27px;
    letter-spacing: 5.6px;
    margin-right: -5.6px;
    line-height: 1;
    white-space: nowrap;
  }
  .banner__headline {
    font-family: "Playfair Display", serif;
    font-weight: 400;
    font-size: 96px;
    letter-spacing: 20px;
    margin-right: -20px;
    line-height: 1;
    margin-top: 8px;
  }
  .banner__tagline {
    font-family: "Crimson Text", serif;
    font-size: 20px;
    line-height: 1.25;
    margin-top: 12px;
  }
  .banner__button {
    display: block;
    width: 295px;
    height: 46px;
    margin: 30px auto 0;
    background: var(--ink-white);
    color: var(--button-text);
    font-family: "Poppins", sans-serif;
    font-weight: 400;
    font-size: 19px;
    letter-spacing: 1.6px;
    line-height: 46px;
    text-decoration: none;
  }
</style>
</head>
<body>
  <section class="banner">
    <svg class="banner__hearts" viewBox="0 0 1200 356" aria-hidden="true">
      <g opacity="0.09">
        <path transform="translate(60 60) scale(1.6)" d="M20 36 C8 27 0 19 0 10 C0 4 5 0 10 0 C14 0 18 3 20 7 C22 3 26 0 30 0 C35 0 40 4 40 10 C40 19 32 27 20 36 Z"/>
        <path transform="translate(40 230) scale(1.1)" d="M20 36 C8 27 0 19 0 10 C0 4 5 0 10 0 C14 0 18 3 20 7 C22 3 26 0 30 0 C35 0 40 4 40 10 C40 19 32 27 20 36 Z"/>
        <path transform="translate(520 40) scale(0.9)" d="M20 36 C8 27 0 19 0 10 C0 4 5 0 10 0 C14 0 18 3 20 7 C22 3 26 0 30 0 C35 0 40 4 40 10 C40 19 32 27 20 36 Z"/>
        <path transform="translate(505 270) scale(1.3)" d="M20 36 C8 27 0 19 0 10 C0 4 5 0 10 0 C14 0 18 3 20 7 C22 3 26 0 30 0 C35 0 40 4 40 10 C40 19 32 27 20 36 Z"/>
        <path transform="translate(120 160) scale(0.7)" d="M20 36 C8 27 0 19 0 10 C0 4 5 0 10 0 C14 0 18 3 20 7 C22 3 26 0 30 0 C35 0 40 4 40 10 C40 19 32 27 20 36 Z"/>
      </g>
    </svg>
    <svg class="banner__photo" viewBox="0 0 1200 356" role="img" aria-label="Photo of a grey buttoned upholstered bed with wingback headboard, white linen, knitted throw, against a concrete wall">
      <defs>
        <linearGradient id="photoTone" x1="0" y1="0" x2="1" y2="1">
          <stop offset="0" stop-color="#c9c9c8"/>
          <stop offset="0.35" stop-color="#8a8c98"/>
          <stop offset="0.6" stop-color="#b7b5b2"/>
          <stop offset="1" stop-color="#e4e3e0"/>
        </linearGradient>
      </defs>
      <path d="M610 0 Q520 190 560 356 L1200 356 L1200 0 Z" fill="#ffffff" opacity="0.12"/>
      <path d="M645 0 Q555 195 588 356 L1200 356 L1200 0 Z" fill="url(#photoTone)"/>
    </svg>
    <div class="banner__copy">
      <p class="banner__kicker">FIND A LOOK YOU</p>
      <h1 class="banner__headline">LOVE</h1>
      <p class="banner__tagline">Lorem ipsum not sure what the rest of<br>this will say at the moment</p>
      <a class="banner__button" href="#">SHOP BEDROOMS</a>
    </div>
  </section>
</body>
</html>
```